Kelvane Plumbing Business cards

Company is Kelvane Plumbing.
name Dashel Morrowby, I am a plumber, drainer, gasfitter and roofer
Mobile: 0431 906 154
Email address: info@kelvaneplumbing.example (check out my website for some ideas)
Website: www.kelvaneplumbing.example
ABN: 82 916 203 471
LIC: 604517K

I am reliable all round plumber. I am a 24 hour emergency service. Kelvane Plumbing is a professional plumbing service in the Illawarra, South Coast, Southern Sydney and Southern Highland regions of NSW. We offer a 24 hour emergency service for piece of mind to our customers. Call us now to see how we can help you. Kelvane Plumbing approaches every job with attention to detail and excellent customer service. With our superior workmanship you can be confident that the job will be done right the first time around. You can rest assured with results that are guaranteed to last.

Target Market(s)

the general public

Contact Information for Business Card

look up website for some ideas something with similar colours to logo and new modern and to catch the eye.

Colors
fdfdfd
ffffff
000000
7f7f7f
aaaaaa
33a6d7
0492cd

Requirements
Must have
• all contact details
• company- Kelvane Plumbing
• name- Dashel Morrowby
• number mobile- 0431 906 154
• Email address- info@kelvaneplumbing.example
• Website- www.kelvaneplumbing.example
• ABN- 82 916 203 471
• LIC- 604517K

```html
<!DOCTYPE html>
<html lang="en">
<head>
<meta charset="utf-8">
<title>Kelvane Plumbing – Business Cards</title>
<link rel="stylesheet" href="https://fonts.googleapis.com/css2?family=Roboto:wght@400;500;700&display=swap">
<style>
  :root {
    --backdrop: #d6e8ef;
    --card-black: #000000;
    --brand-blue: #0492cd;
    --brand-blue-light: #33a6d7;
    --ribbon-grey: #7f7f7f;
    --ribbon-shade: #aaaaaa;
    --text-white: #ffffff;
    --text-soft: #fdfdfd;
  }
  * { box-sizing: border-box; margin: 0; padding: 0; }
  html, body {
    width: 1200px; height: 900px; overflow: hidden;
    background: var(--backdrop);
    font-family: "Roboto", Arial, sans-serif;
  }
  .canvas {
    position: relative; width: 1200px; height: 900px;
  }
  .card {
    position: absolute;
    width: 560px; height: 320px;
    border-radius: 18px;
    background: var(--card-black);
    overflow: hidden;
  }
  .card--front { left: 320px; top: 90px; }
  .card--back { left: 320px; top: 490px; }

  /* Front */
  .front-brand {
    position: absolute; left: 0; right: 0; top: 118px;
    display: flex; align-items: center; justify-content: center; gap: 14px;
  }
  .brand-dot {
    width: 22px; height: 22px; border-radius: 50%;
    background: var(--brand-blue);
  }
  .brand-name {
    color: var(--brand-blue-light);
    font-weight: 700; font-size: 42px; letter-spacing: 1px;
  }
  .front-web {
    position: absolute; left: 0; right: 0; bottom: 44px;
    text-align: center; color: var(--text-white);
    font-size: 13px; letter-spacing: 0.3px;
  }

  /* Back */
  .back-panel { position: absolute; inset: 0; }
  .back-brand {
    position: absolute; left: 40px; top: 110px;
    display: flex; align-items: center; gap: 10px;
  }
  .back-brand .brand-name { font-size: 22px; }
  .back-brand .brand-dot { width: 14px; height: 14px; }

  .ribbon {
    position: absolute; left: 236px; top: 40px;
    width: 290px; height: 54px;
    background: var(--ribbon-grey);
    padding: 9px 0 0 24px;
    color: var(--text-white);
  }
  .ribbon-name { font-size: 19px; font-weight: 700; }
  .ribbon-role { font-size: 9.5px; margin-top: 2px; color: var(--text-soft); }

  .contact-list {
    position: absolute; left: 44px; bottom: 34px;
    list-style: none;
  }
  .contact-item {
    display: flex; align-items: center; gap: 12px;
    color: var(--text-white); font-size: 13px;
    margin-top: 8px;
  }
  .contact-icon {
    width: 18px; height: 18px; background: var(--brand-blue);
    display: flex; align-items: center; justify-content: center;
  }

  .address-block {
    position: absolute; left: 350px; top: 148px; width: 200px;
    text-align: center; color: var(--text-white);
    font-size: 12.5px; line-height: 1.5;
  }
  .address-pin { display: block; margin: 0 auto 8px; }
</style>
</head>
<body>
<main class="canvas">

  <section class="card card--front" aria-label="Card front">
    <div class="front-brand">
      <span class="brand-dot"></span>
      <span class="brand-name">Kelvane Plumbing</span>
    </div>
    <p class="front-web">www.kelvaneplumbing.example</p>
  </section>

  <section class="card card--back" aria-label="Card back">
    <svg class="back-panel" width="560" height="320" viewBox="0 0 560 320">
      <polygon points="250,0 560,0 560,320 372,320" fill="var(--brand-blue)"/>
      <polygon points="236,94 274,94 274,118" fill="#555555"/>
    </svg>

    <div class="back-brand">
      <span class="brand-dot"></span>
      <span class="brand-name">Kelvane Plumbing</span>
    </div>

    <div class="ribbon">
      <p class="ribbon-name">Dashel Morrowby</p>
      <p class="ribbon-role">Plumber, Drainer, Gasfitter &amp; Roofer</p>
    </div>

    <ul class="contact-list">
      <li class="contact-item">
        <span class="contact-icon">
          <svg width="12" height="12" viewBox="0 0 24 24"><path fill="#fff" d="M6.6 10.8a15 15 0 0 0 6.6 6.6l2.2-2.2c.3-.3.7-.4 1-.2 1.1.4 2.3.6 3.6.6.6 0 1 .4 1 1V20c0 .6-.4 1-1 1A17 17 0 0 1 3 4c0-.6.4-1 1-1h3.5c.6 0 1 .4 1 1 0 1.3.2 2.5.6 3.6.1.3 0 .7-.2 1z"/></svg>
        </span>0431 906 154
      </li>
      <li class="contact-item">
        <span class="contact-icon">
          <svg width="12" height="12" viewBox="0 0 24 24"><rect x="2" y="5" width="20" height="14" fill="none" stroke="#fff" stroke-width="2"/><path d="M2 5l10 8 10-8" fill="none" stroke="#fff" stroke-width="2"/></svg>
        </span>info@kelvaneplumbing.example
      </li>
      <li class="contact-item">
        <span class="contact-icon">
          <svg width="12" height="12" viewBox="0 0 24 24"><circle cx="12" cy="12" r="9" fill="none" stroke="#fff" stroke-width="2"/><path d="M3 12h18M12 3c3 3 3 15 0 18M12 3c-3 3-3 15 0 18" fill="none" stroke="#fff" stroke-width="1.6"/></svg>
        </span>www.kelvaneplumbing.example
      </li>
    </ul>

    <div class="address-block">
      <svg class="address-pin" width="14" height="18" viewBox="0 0 24 32"><path fill="#fff" d="M12 0a11 11 0 0 0-11 11c0 8 11 21 11 21s11-13 11-21A11 11 0 0 0 12 0zm0 15a4 4 0 1 1 0-8 4 4 0 0 1 0 8z"/></svg>
      <p>1234 Full address - Harwick Bay</p>
      <p>Northvale 12345</p>
      <p>ABN- 82 916 203 471</p>
      <p>LIC- 604517K</p>
    </div>
  </section>

</main>
</body>
</html>
```